Gelato Business Card

create a new business card using existing logo

Target Market(s)

B2B

Contact Information for Business Card

typical contact info: logo, address, email, phone, rep name

Colors
0355a3
33a6d7

Requirements
Must have
• a feel of high quality, luxury, happiness
• use cool, comforting color and texture of business card.
Nice to have
• "A Little Perfection Goes A Long Way!" TM
• or, "more quality, more flavor"
• or, "Flavor Matters"

```html
<!DOCTYPE html>
<html lang="en">
<head>
<meta charset="utf-8">
<title>Bellaluna Gelato Business Card</title>
<link rel="stylesheet" href="https://fonts.googleapis.com/css2?family=Montserrat:wght@300;600&family=Quicksand:wght@400;500;700&display=swap">
<style>
  :root {
    --backdrop: #e4e5e7;
    --charcoal: #414042;
    --violet: #52429a;
    --apricot: #f8a24a;
    --paper: #ffffff;
    --teal: #5cc2bf;
    --ink-light: #f2f2f2;
  }
  * { margin: 0; padding: 0; box-sizing: border-box; }
  html, body {
    width: 1200px; height: 1200px; overflow: hidden;
    background: var(--backdrop);
  }
  .canvas { position: relative; width: 1200px; height: 1200px; }
  .card {
    position: absolute; left: 276px;
    width: 1050px; height: 600px;
    transform: scale(0.621); transform-origin: 0 0;
    overflow: hidden;
    font-family: "Quicksand", sans-serif;
  }
  .card--front { top: 155px; }
  .card--back { top: 661px; }
  .card-art { position: absolute; inset: 0; width: 100%; height: 100%; }

  .rep { position: absolute; left: 96px; top: 114px; color: var(--ink-light); }
  .rep-name { font-family: "Montserrat", sans-serif; font-size: 40px; letter-spacing: 0.5px; line-height: 1; }
  .rep-name .first { font-weight: 600; }
  .rep-name .last { font-weight: 300; }
  .rep-title { font-family: "Montserrat", sans-serif; font-weight: 400; font-size: 21px; letter-spacing: 0.8px; margin-top: 12px; }

  .contacts { position: absolute; left: 96px; top: 239px; list-style: none; }
  .contact { display: flex; align-items: center; color: var(--ink-light); font-size: 23px; font-weight: 500; line-height: 1.2; }
  .contact + .contact { margin-top: 24px; }
  .contact-icon { width: 52px; height: 52px; flex: none; margin-right: 18px; }

  .brand {
    position: absolute; display: flex; align-items: center; gap: 14px;
    font-family: "Quicksand", sans-serif; font-weight: 700; font-size: 52px;
    color: var(--violet); letter-spacing: 1px;
  }
  .brand-dot { width: 30px; height: 30px; border-radius: 50%; background: var(--violet); }
  .card--front .brand { left: 640px; top: 282px; }
  .card--back .brand { left: 140px; top: 272px; }

  .site { position: absolute; left: 705px; top: 490px; display: flex; align-items: center; }
  .site-text { font-size: 23px; font-weight: 500; color: var(--ink-light); }
  .site-text .accent { color: var(--apricot); }
  .site-rule { position: absolute; left: 222px; top: 16px; width: 124px; height: 3px; background: var(--apricot); }
</style>
</head>
<body>
<main class="canvas">

  <section class="card card--front" aria-label="Business card front">
    <svg class="card-art" viewBox="0 0 1050 600" aria-hidden="true">
      <rect width="1050" height="600" fill="var(--charcoal)"/>
      <path fill="var(--violet)" d="M330 0 C430 60 480 200 550 355 L600 450 L1050 450 L1050 0 Z"/>
      <path fill="var(--apricot)" d="M583 0 C535 110 520 250 548 355 C560 400 575 420 590 430 L1050 430 L1050 0 Z"/>
      <path fill="var(--paper)" d="M750 0 C620 90 562 230 570 330 C578 440 640 540 720 600 L1050 600 L1050 0 Z"/>
      <rect x="350" y="0" width="375" height="2" fill="var(--teal)"/>
    </svg>

    <div class="rep">
      <p class="rep-name"><span class="first">DARIO</span><span class="last">VENTI</span></p>
      <p class="rep-title">CREATIVE DESIGNER</p>
    </div>

    <ul class="contacts">
      <li class="contact">
        <svg class="contact-icon" viewBox="0 0 52 52" aria-hidden="true">
          <circle cx="26" cy="26" r="23.5" fill="none" stroke="var(--apricot)" stroke-width="3"/>
          <path fill="var(--apricot)" d="M20 18c1-1 2-1 3 0l2 3c.5 1 .3 2-.5 2.6l-1 .8c1 2 2.5 3.6 4.4 4.6l.8-1c.6-.8 1.6-1 2.6-.5l3 2c1 1 1 2 0 3l-1 1c-1 1-3 1.2-5 .2-4-2-7-5-9-9-1-2-.8-4 .2-5z"/>
        </svg>
        +000 12345 6789
      </li>
      <li class="contact">
        <svg class="contact-icon" viewBox="0 0 52 52" aria-hidden="true">
          <circle cx="26" cy="26" r="23.5" fill="none" stroke="var(--apricot)" stroke-width="3"/>
          <path fill="var(--apricot)" d="M34 18 L19 25 L25 27 L27 33 Z"/>
        </svg>
        urname@bellaluna.com
      </li>
      <li class="contact">
        <svg class="contact-icon" viewBox="0 0 52 52" aria-hidden="true">
          <circle cx="26" cy="26" r="23.5" fill="none" stroke="var(--apricot)" stroke-width="3"/>
          <path fill="var(--apricot)" d="M26 16c-4 0-7 3-7 7 0 5 7 13 7 13s7-8 7-13c0-4-3-7-7-7zm0 10a3 3 0 1 1 0-6 3 3 0 0 1 0 6z"/>
        </svg>
        <span>Street Address Here<br>Singapore, 2222</span>
      </li>
      <li class="contact">
        <svg class="contact-icon" viewBox="0 0 52 52" aria-hidden="true">
          <circle cx="26" cy="26" r="23.5" fill="none" stroke="var(--apricot)" stroke-width="3"/>
          <g fill="var(--apricot)">
            <circle cx="31" cy="19" r="3.5"/><circle cx="20" cy="26" r="3.5"/><circle cx="31" cy="33" r="3.5"/>
          </g>
          <path d="M31 19 L20 26 L31 33" fill="none" stroke="var(--apricot)" stroke-width="2"/>
        </svg>
        Bellaluna.com
      </li>
    </ul>

    <p class="brand"><span class="brand-dot"></span>Bellaluna</p>
  </section>

  <section class="card card--back" aria-label="Business card back">
    <svg class="card-art" viewBox="0 0 1050 600" aria-hidden="true">
      <rect width="1050" height="600" fill="var(--charcoal)"/>
      <path fill="var(--violet)" d="M0 0 L880 0 C790 60 720 220 665 345 L625 440 L0 440 Z"/>
      <path fill="var(--apricot)" d="M0 0 L628 0 C670 100 690 240 675 340 C668 390 650 415 630 435 L0 435 Z"/>
      <path fill="var(--paper)" d="M0 0 L463 0 C580 100 650 220 642 330 C635 440 570 530 492 600 L0 600 Z"/>
    </svg>

    <p class="brand"><span class="brand-dot"></span>Bellaluna</p>

    <div class="site">
      <p class="site-text">www.<span class="accent">bellaluna</span>.com</p>
      <span class="site-rule"></span>
    </div>
  </section>

</main>
</body>
</html>
```